KBMR new business card design

We need a business card design for our established business which is Australia wide however based in Melbourne. We are a young team of Financial Planners who specialize in Insurance and Basic super advice for people like us.

We are people who help our clients get things done in a timely and cost effective manner whilst having a good time and a laugh along the way.

We would like this to have a consistent feel with our new e-brochure which i have attached from a color and font perspective.

Industry/Entity Type

Business

Requirements
Must have
• We do not need specific address details rather just the states we are in:

VIC/NSW/QLD/TAS
Nice to have
• Curved edge to mate the brochure

```html
<!DOCTYPE html>
<html lang="en">
<head>
<meta charset="utf-8">
<title>KBMR Business Card</title>
<link rel="stylesheet" href="https://fonts.googleapis.com/css2?family=Questrial&family=Mulish:ital,wght@0,400;0,700;0,800;1,400&display=swap">
<style>
  :root {
    --backdrop: #2b2b2b;
    --card: #ffffff;
    --card-shade: #e9e9e9;
    --leaf-green: #8dc63f;
    --leaf-green-deep: #76a83a;
    --brand-green: #00a651;
    --ink: #1e1e1e;
    --ink-soft: #4d4d4d;
  }
  * { margin: 0; padding: 0; box-sizing: border-box; }
  html, body {
    width: 1200px; height: 900px; overflow: hidden;
    background: var(--backdrop);
  }
  .stage { position: relative; width: 1200px; height: 900px; }

  .card {
    position: absolute; top: 106px; width: 411px; height: 666px;
    background: var(--card); overflow: hidden;
  }
  .card--front { left: 172px; border-bottom-right-radius: 80px; }
  .card--back {
    left: 667px; border-bottom-left-radius: 80px;
    background: radial-gradient(circle at 30% 20%, var(--card) 45%, var(--card-shade) 100%);
  }

  .leaf-pattern {
    position: absolute; left: 28px; top: 24px; width: 358px; height: 212px;
    background: linear-gradient(160deg, rgba(141,198,63,0.28), rgba(141,198,63,0.10));
    border-radius: 4px;
  }

  .brand {
    position: absolute; display: flex; align-items: center; gap: 10px;
    font-family: "Mulish", sans-serif; font-weight: 800; color: var(--brand-green);
  }
  .brand__square { background: var(--leaf-green); }
  .card--front .brand { left: 31px; top: 330px; font-size: 34px; }
  .card--front .brand__square { width: 34px; height: 34px; }
  .card--back .brand { left: 137px; top: 255px; font-size: 36px; }
  .card--back .brand__square { width: 36px; height: 36px; }

  .contact {
    position: absolute; left: 31px; top: 424px;
    font-family: "Questrial", sans-serif; color: var(--ink);
  }
  .contact__name {
    font-family: "Mulish", sans-serif; font-weight: 800; font-size: 15px;
    letter-spacing: 0.6px; color: var(--leaf-green); line-height: 17px;
  }
  .contact__role {
    font-family: "Mulish", sans-serif; font-weight: 700; font-size: 12px;
    letter-spacing: 0.6px; color: var(--leaf-green); line-height: 15px;
  }
  .contact__licence {
    margin-top: 3px; font-family: "Mulish", sans-serif; font-style: italic;
    font-size: 11px; line-height: 12px; color: var(--ink-soft);
  }
  .contact__phones { margin-top: 4px; font-size: 12.5px; line-height: 13px; letter-spacing: 0.6px; }
  .contact__phones dt { float: left; width: 18px; color: var(--leaf-green); }
  .contact__phones dd { margin-left: 18px; }
  .contact__lines { margin-top: 3px; font-size: 12.5px; line-height: 14px; letter-spacing: 0.6px; }

  .services {
    position: absolute; left: 137px; top: 366px;
    font-family: "Questrial", sans-serif; font-size: 13px; line-height: 16px;
    color: var(--ink); letter-spacing: 0.4px; list-style: none;
  }
  .services__title { color: #000; }

  .accent-shape {
    position: absolute; left: 137px; top: 464px; width: 136px; height: 202px;
    background: linear-gradient(180deg, var(--leaf-green) 30%, var(--leaf-green-deep) 100%);
    border-top-left-radius: 40px; border-top-right-radius: 68px;
  }
</style>
</head>
<body>
<main class="stage">
  <section class="card card--front" aria-label="Business card front">
    <div class="leaf-pattern" role="img" aria-label="Scattered green leaf pattern"></div>
    <div class="brand"><span class="brand__square"></span><span>KBMR</span></div>
    <div class="contact">
      <p class="contact__name">Daniel Whitford</p>
      <p class="contact__role">Financial Adviser</p>
      <p class="contact__licence">KBMR Planning Pty Ltd<br>Authorised Representatives<br>Meridian Wealth Partners Limited<br>Australian Financial Services Licensee</p>
      <dl class="contact__phones">
        <dt>p</dt><dd>1300 555 214</dd>
        <dt>f</dt><dd>03 9555 0148</dd>
        <dt>m</dt><dd>0400 555 729</dd>
      </dl>
      <p class="contact__lines">NSW VIC TAS QLD<br>daniel@kbmr.com.au<br>www.kbmr.com.au</p>
    </div>
  </section>

  <section class="card card--back" aria-label="Business card back">
    <div class="brand"><span class="brand__square"></span><span>KBMR</span></div>
    <ul class="services">
      <li class="services__title">Specialising in:</li>
      <li>Risk Insurance</li>
      <li>Debt Management</li>
      <li>Superannuation</li>
      <li>Wealth Creation</li>
      <li>Retirement Planning</li>
    </ul>
    <div class="accent-shape"></div>
  </section>
</main>
</body>
</html>
```